Design Website Templates for Photographers for Lumora Inc. (bookwrenlyte.example)

Lumora Inc. is a generative website company for wedding photographers.
We are seeking new photography website design inspirations for the next template to be offered on our platform. The catch is you must use the same data for your designs. You also must use all of the data somewhere in the design. You cannot add new content besides the data available. If you wish to add any elements It will be hardcoded and must be universally fitting for many different photographers. We recommend not using any hardcoded test.
Don't be afraid to be creative! Although the most important element of a photographers website is the photos, we are looking for unique and out-of-the-box designs for the actual site as well.
Here is the User generated data available to you:
- 4 Hero Images Landscape, 4 Hero Images Portrait
- Tagline “destination photographer based in Maui, Hawaii”
- “About Photo” of the photographer
- “About” Biography Text
- The design can use up to 3 colors + background color and 2 fonts
- 9 Gallery images
- 3 Packages/services that include landscape/portrait images, a price, a title and text
- Testimonials made up of an image, text and text for the name of testimonial giver
See some examples of our current website designs attached. You can use any of the data you see in the designs.
Updates
We are looking for designs that are less feminine and are more neutral in color and fonts. Currently our templates are more oriented towards feminine photographers. We want to have designs that speak to diverse audiences. We thank everyone for submitting and are reviewing the designs.
Number of Pages Required
1 page
Look and feel
Each slider illustrates characteristics of the customer's brand and the style your logo design should communicate.

```html
<!DOCTYPE html>
<html lang="en">
<head>
<meta charset="utf-8">
<title>Lumora — Destination Photographer</title>
<link href="https://fonts.googleapis.com/css2?family=Jost:wght@300;400;500;600;700&display=swap" rel="stylesheet">
<style>
:root{
  --ink:#14212c;
  --navy:#1d2b37;
  --deep:#0b1823;
  --gold:#f3b432;
  --paper:#ffffff;
  --sand:#f4f2ed;
  --foot:#f8f7f3;
  --grey:#8a8d90;
  --muted:#4a5560;
}
*{margin:0;padding:0;box-sizing:border-box}
html,body{width:1200px;height:4096px;overflow:hidden}
body{font-family:"Jost",sans-serif;color:var(--ink);background:var(--paper);position:relative}
.abs{position:absolute}
.photo{position:absolute}

/* hero */
.hero{position:absolute;left:0;top:0;width:1200px;height:723px;background:linear-gradient(120deg,#223240 0%,#1a2834 55%,#2a3945 100%)}
.logo{position:absolute;left:48px;top:28px;font-size:36px;font-weight:400;letter-spacing:2px;color:#fff;display:flex;align-items:center;gap:8px}
.logo .dot{width:10px;height:10px;border-radius:50%;background:var(--gold)}
.nav{position:absolute;top:40px;left:455px;font-size:12px;color:#fff;letter-spacing:.3px}
.nav span{position:absolute;white-space:nowrap}
.book-btn{position:absolute;left:1017px;top:29px;width:132px;height:37px;border:1px solid #fff;color:#fff;font-size:12px;display:flex;align-items:center;justify-content:center}
.hero-block{left:72px;top:172px;width:211px;height:316px;background:var(--gold)}
.hero-photo{left:94px;top:224px;width:426px;height:499px;background:linear-gradient(180deg,#c9c4bc 0%,#a9a49a 35%,#d9cbb5 70%,#cdb796 100%)}
.social{left:1050px;top:94px;width:72px;height:198px;background:#7c7f83}
.social i{position:absolute;left:28px;width:16px;height:16px;border-radius:50%;background:#fff}
.follow{left:1074px;top:242px;width:26px;height:92px;background:var(--gold);color:#fff;font-size:9px;writing-mode:vertical-rl;display:flex;align-items:center;justify-content:center;letter-spacing:.5px}
.headline{left:548px;top:270px;font-size:58px;line-height:54px;font-weight:700;color:#fff;text-transform:uppercase;letter-spacing:-.5px}
.hero-copy{left:764px;top:567px;width:300px;font-size:14px;line-height:24px;color:#fff;font-weight:300}

/* about */
.about-title{left:151px;top:785px;font-size:58px;line-height:66px;font-weight:400;z-index:3;white-space:nowrap}
.about-frame{left:323px;top:963px;width:243px;height:326px;border-left:13px solid var(--gold);border-bottom:13px solid var(--gold)}
.about-photo{left:337px;top:857px;width:373px;height:418px;background:linear-gradient(160deg,#eceae6 0%,#c9a27d 45%,#9a8f86 100%)}
.bio{left:764px;top:856px;width:290px;font-size:12.4px;line-height:21.8px;color:var(--muted);font-weight:300}
.bio p{margin-bottom:21.8px}

/* recent work */
.work-mark{left:394px;top:1383px;width:210px;height:36px;background:var(--gold)}
.work-title{left:267px;top:1362px;font-size:58px;font-weight:500;line-height:70px}
.work-sub{left:396px;top:1445px;font-size:14px;line-height:24px;color:var(--muted);font-weight:300}
.gallery-item{position:absolute;top:1527px;width:285px}
.gallery-item .photo{position:relative;width:285px;height:374px}
.gallery-item p{margin-top:16px;font-size:13.5px;color:var(--muted);white-space:nowrap;font-weight:300}

/* split promos */
.promo-dark{left:0;top:2003px;width:600px;height:346px;background:var(--deep);color:#fff;text-align:center}
.promo-gold{left:600px;top:2349px;width:600px;height:341px;background:var(--gold);color:var(--ink);text-align:center}
.promo h3{font-size:29px;font-weight:400;line-height:33px}
.btn{display:inline-flex;align-items:center;justify-content:center;font-size:11.5px;font-weight:600;letter-spacing:.4px}
.promo .lead{font-size:15px}
.promo .tags{font-size:13px;line-height:22px;font-weight:300}

/* client love */
.section-title{left:0;width:1200px;text-align:center;font-size:31px;font-weight:500;color:#13304a}
.card{position:absolute;top:2829px;width:284px;height:405px;border:1px solid #d8d6d2;text-align:center}
.card.filled{background:var(--sand);border-color:var(--sand)}
.card .quote{margin-top:32px;height:50px;font-size:90px;line-height:90px;color:#a7a9ac;font-weight:700}
.card p{margin:22px auto 0;width:230px;font-size:13.5px;line-height:22.6px;color:var(--muted);font-weight:300}
.card hr{width:50px;margin:27px auto 0;border:0;border-top:1px solid #333}
.card .name{margin-top:12px;font-size:15px}

/* form */
.contact-form{left:304px;top:3368px;width:592px}
.contact-form label{display:block;font-size:10.5px;color:var(--muted);height:15px}
.contact-form .field{height:33px;background:var(--sand);margin-bottom:22px}
.contact-form .area{height:88px;background:var(--sand)}
.submit{left:548px;top:3699px;width:102px;height:37px;background:var(--gold);color:#fff}

/* footer */
.footer{left:0;top:3780px;width:1200px;height:316px;background:var(--foot)}
.foot-col{position:absolute;top:53px;font-size:11.5px;line-height:21.8px;color:var(--muted);font-weight:300}
.foot-col h4{font-size:12px;font-weight:600;color:var(--ink);margin-bottom:6px}
.copyright{position:absolute;top:259px;width:1200px;text-align:center;font-size:11.5px;color:var(--muted)}
</style>
</head>
<body>

<header class="hero" role="img" aria-label="Dim background photograph of a couple resting in bed">
  <div class="logo">LUMORA<span class="dot"></span></div>
  <nav class="nav">
    <span style="left:0">ABOUT</span>
    <span style="left:90px">BLOG</span>
    <span style="left:175px">TESTIMONIALS</span>
    <span style="left:310px">PORTFOLIO</span>
    <span style="left:427px">GET IN TOUCH</span>
  </nav>
  <div class="book-btn">BOOK WITH ME</div>
</header>
<div class="abs hero-block"></div>
<div class="photo hero-photo" role="img" aria-label="Couple embracing on a sandy beach by the sea with a small island behind"></div>
<div class="abs social" aria-label="Social links">
  <i style="top:30px"></i><i style="top:70px"></i><i style="top:112px"></i>
</div>
<div class="abs follow">FOLLOW ME</div>
<h1 class="abs headline">Destination<br>Photographer<br>Based in<br>Maui, Hawaii</h1>
<p class="abs hero-copy">Professional commercial photography to elevate your business Lorem ipsum dolor sit amet consectetur. Duis quis amet nunc vulputate dolor scelerisque.</p>

<div class="abs about-frame"></div>
<div class="photo about-photo" role="img" aria-label="Portrait of the photographer with long hair in a grey knit sweater"></div>
<h2 class="abs about-title">About<br>Mara Ellison</h2>
<div class="abs bio">
  <p>Immerse yourself in the mesmerizing world of landscape photography. From majestic mountains to serene seascapes, our images showcase the awe-inspiring beauty of nature. Lorem ipsum dolor sit amet consectetur. Duis quis amet nunc vulputate pellentesque massa mi aliquam.</p>
  <p>Fusce semper aliquam egestas mauris est nunc. Et pellentesque sodales elementum cursus mattis suscipit etiam nulla odio. Molestie tristique cursus ipsum non vitae nibh amet lacus. Orci dictum erat vitae at at non massa. Sit sit nisl pretium quisque ornare nunc posuere nunc.</p>
  <p>Etat est varius pulvinar sodales massa pulvinar risus. Orci at ipsum tellus posuere nunc. Auctor malesuada placerat scelerisque est. Sed tellus sit cras lectus risus ante. Scelerisque cursus risus sodales habitasse nibh volutpat.</p>
</div>

<div class="abs work-mark"></div>
<h2 class="abs work-title">Recent Work</h2>
<p class="abs work-sub">Professional commercial photography to elevate your business<br>Lorem ipsum dolor sit amet consectetur.</p>
<div class="gallery-item" style="left:150px"><div class="photo" role="img" aria-label="Hiker on a rocky summit facing misty mountains at sunrise" style="background:linear-gradient(180deg,#d9c7a8 0%,#e8b98a 40%,#8f98a0 75%,#3d3a36 100%)"></div><p>Cozy at Home Couples Session</p></div>
<div class="gallery-item" style="left:458px"><div class="photo" role="img" aria-label="Person with a laptop on a bed beside a sleeping dog" style="background:linear-gradient(180deg,#c9c3bb 0%,#a89e94 45%,#c58f52 70%,#d8d4ce 100%)"></div><p>Cozy at Home Couples Session</p></div>
<div class="gallery-item" style="left:765px"><div class="photo" role="img" aria-label="Studio portrait of a woman in a black blouse against a dark backdrop" style="background:linear-gradient(180deg,#2e3034 0%,#4b4340 50%,#1c1c1e 100%)"></div><p>Cozy at Home Couples Session</p></div>
<div class="gallery-item" style="left:1073px"><div class="photo" role="img" aria-label="Beach with a small island under a cloudy sky" style="background:linear-gradient(180deg,#b9c3c9 0%,#d7d6d0 45%,#cdb594 100%)"></div><p>Cozy at Home Couples Session</p></div>

<section class="abs promo promo-dark">
  <h3 style="margin-top:75px">Are you a photographer?</h3>
  <div class="btn" style="margin-top:19px;width:202px;height:35px;background:var(--gold);color:var(--ink)">GET STARTED HERE</div>
  <p class="lead" style="margin-top:21px">Level the playing field with Lumora.</p>
  <p class="tags" style="margin-top:16px">Website * Package * Galleries * Bookings * Payments<br>Contacts * Automated SEO * All-in-One</p>
</section>
<div class="photo" role="img" aria-label="Couple lying close together on a bed" style="left:600px;top:2003px;width:600px;height:346px;background:linear-gradient(135deg,#3f4f57 0%,#b08f6d 40%,#7f94a0 75%,#4e6470 100%)"></div>
<div class="photo" role="img" aria-label="Photographer holding a camera by its strap on a path" style="left:0;top:2349px;width:600px;height:341px;background:linear-gradient(135deg,#1f2226 0%,#6e6f6d 45%,#a9a69e 75%,#5d5e5a 100%)"></div>
<section class="abs promo promo-gold">
  <h3 style="margin-top:73px">Are you looking to book a<br>photographer?</h3>
  <div class="btn" style="margin-top:13px;width:187px;height:35px;background:var(--deep);color:#fff">VISIT THE MARKETPLACE</div>
  <p class="lead" style="margin-top:13px">Browse over 1000+ photographers to find the ferfect match.</p>
  <p class="tags" style="margin-top:6px;color:var(--muted)">Weddings * Family * Newborn * Headshots * and More</p>
</section>

<h2 class="abs section-title" style="top:2756px">CLIENT LOVE</h2>
<div class="card" style="left:150px"><div class="quote">“</div><p>We loved our time here at your wonderful studio. A special place with exceptional attention to detail. Lorem ipsum dolor sit amet consectetur. Duis quis amet nunc vulputate pellentesque massa mi aliquam. Fusce semper aliquam egestas mauris est nunc. Et pellentesque sodales elementum cursus mattis suscipit etiam nulla odio.</p><hr><div class="name">Mara Ellison</div></div>
<div class="card filled" style="left:458px"><div class="quote">“</div><p>We loved our time here at your wonderful studio. A special place with exceptional attention to detail. Lorem ipsum dolor sit amet consectetur. Duis quis amet nunc vulputate pellentesque massa mi aliquam. Fusce semper aliquam egestas mauris est nunc. Et pellentesque sodales elementum cursus mattis suscipit etiam nulla odio.</p><hr><div class="name">Mara Ellison</div></div>
<div class="card" style="left:765px"><div class="quote">“</div><p>We loved our time here at your wonderful studio. A special place with exceptional attention to detail. Lorem ipsum dolor sit amet consectetur. Duis quis amet nunc vulputate pellentesque massa mi aliquam. Fusce semper aliquam egestas mauris est nunc. Et pellentesque sodales elementum cursus mattis suscipit etiam nulla odio.</p><hr><div class="name">Mara Ellison</div></div>

<h2 class="abs section-title" style="top:3296px">LET’S CONNECT</h2>
<form class="abs contact-form">
  <label>Full Name</label><div class="field"></div>
  <label>Email Address</label><div class="field"></div>
  <label>Phone Number</label><div class="field"></div>
  <label>Tell me about yourself</label><div class="area"></div>
</form>
<div class="abs btn submit">SUBMIT</div>

<footer class="abs footer">
  <div class="foot-col" style="left:150px"><h4>Book a Photographer</h4>How it works<br>About<br>Blog<br>FAQ<br>Terms of Service</div>
  <div class="foot-col" style="left:380px"><h4>For Photographers</h4>Pricing<br>Knowledge Base<br>Free Membership<br>Blog<br>FAQ<br>Policies<br>Terms of Service</div>
  <div class="foot-col" style="left:613px"><h4>Company</h4>About<br>Contact<br>Careers</div>
  <div class="foot-col" style="left:841px"><h4>Contact</h4>contact@bookwrenlyte.example<br>+1 555 014 2290<br>88 Harbour Lane, Victoria,<br>BC V0V 0A0</div>
  <div class="copyright">© 2023 LUMORA - All Rights Reserved.</div>
</footer>

</body>
</html>
```